author needs a Book Cover design

Needs a book cover design that matches the title in some way.
Book Title is- 9 Lanterns Beyond the Quiet Harbor at Dusk.
Subtile- Gentle Lessons On Morning Gardens.
Author Name:-Gordon Peltiway, Sr.

Final Design is subject to Book Publisher's requirement.

Font styles to use
Serif

Requirements
Must have
• Follow these recommended specifications for your cover file:
• Page Size: Your cover should be a single (one-piece) PDF that includes the back cover, spine, and front cover. You can submit your cover on any size page as long as the printable area is measured exactly for your book's trim size, spine width, and allows at least .125” bleed, centered horizontally and vertically.
• Minimum Cover Width: Bleed + Back Cover Trim Size + Spine Width + Front Cover Trim Size + Bleed
• Minimum Cover Height: Bleed + Book Height Trim Size + Bleed
• Trim Size: Your cover should be the same trim size as you choose in the Title Information when setting up your book. For example, submitting a cover that was previously used for a 6.25” x 9.25” book would not work for a 6” x 9” book.
• Barcodes: For manufacturing and distribution reasons, your book's back cover must include a valid ISBN barcode. If your cover already has an ISBN barcode, make sure it is high-resolution, or at least 300 dpi, and 1.5" - 2" in width with proportional height. Ideally, this barcode should be 2” wide by 1.2” tall. Also, check to make sure you have the rights to use the ISBN on your cover, because not all services allow you to use their ISBNs elsewhere.
• QR codes: There are no set size restrictions, but the quality (resolution) of the image must be set to at least 300 dpi. Make sure you have the rights to use the code.
• If your artwork does not include a barcode, we will automatically add one in the lower right-hand corner of your book's back cover, free of charge. Our system will place the ISBN barcode in a space 2" wide and 1.2" tall. The bottom of this barcode is located 1/4" up from the bottom trim line of the cover. The right side of the barcode is located 1/4" to the left of the spine. Please ensure that you don't have any important images or text in the barcode location. You can also refer to our Artwork Templates for the exact size and position of the ISBN barcode on your final cover.
• If you don’t have an ISBN already on your cover, but you have live graphic or text elements in the location that our system will place the ISBN, you will need to move those elements or place the ISBN in a different location yourself.
• Publishing Logos: We do not add our logo to your book.
• Spine Width and Variance: If your artwork was created for a different service, please make sure that the spine width of your current cover matches our spine width. Different services may use different paper thickness, which is why the spine width of your cover artwork could be correct for another service but incorrect for our service.
• Ideally, you should avoid hard vertical lines separating your front or back cover panels from your spine and should allow for at least a .125" variance of your spine on each side (for example, the text on a 1" spine should be no larger than .75" wide). For books with a page count of less than 130 pages, we strongly recommend a blank spine.
• Your spine width should be calculated based on the number of pages in your book and using the appropriate formula:
• Black and White Interior Book Spine Width:
• White paper: Number of pages x .002252 = Spine width in inches
• Cream paper: Number of pages x .0025 = Spine width in inches
• Color Interior Book Spine Width:
• Number of pages x .002347 = Spine width in inches
• Example of spine width calculation for a 120-page black and white interior book with white paper:
• 120 x .002252 = .27" spine width
• Text and Image Placement: All live cover elements, or text and images that cannot be cut, must be at least .125" inside the trim lines to ensure no important elements are cut during the bookmaking process and the appearance of your printed books is consistent.
• Bleed: Your cover's background must extend at least .125" beyond the final trim line to accommodate for cutting/trimming tolerance.
• Crop/Registration Marks: Please do not include any crop or registration marks on your files, as they may interfere with the binding process or appear on the cover. We use our own measurements, specific to our systems, for cutting and binding; crop or registration marks placed by you could interfere with this process.
• Images and Fonts: Any images you include on your book's cover may be tagged with your choice of CMYK or RGB profiles or left untagged in a generic color space. All images should be sized at 100%, flattened to one layer and placed in your native document at a resolution of at least 300 DPI. You should also embed all fonts in your PDF file.
• Gordon, I hope this information is helpful to you. Please feel free to contact us if you have any other questions or concerns.
• Best regards,
• *WILL SUPPLY THE PAGE NUMBERS INFORMATION
• Lenora
• PrintHollow Member Services
Nice to have
• An attractive design that matches the title. Design can include backgrounds

```html
<!DOCTYPE html>
<html lang="en">
<head>
<meta charset="utf-8">
<title>9 Lanterns Beyond the Quiet Harbor at Dusk — Cover</title>
<link href="https://fonts.googleapis.com/css2?family=Questrial&family=Playball&display=swap" rel="stylesheet">
<style>
  :root{
    --ink:#111111;
    --crimson:#b3121a;
    --box-red:#9e1216;
    --paper:#ffffff;
    --splash-red:#a8321f;
    --splash-green:#5d6b2a;
    --splash-dark:#2b241c;
    --portrait-grey:#8a8a8a;
  }
  html,body{margin:0;padding:0;overflow:hidden;background:var(--paper);}
  .cover{position:relative;width:1200px;height:879px;background:var(--paper);overflow:hidden;color:var(--ink);font-family:"Questrial",sans-serif;}
  .caps{font-family:"Questrial",sans-serif;text-transform:uppercase;letter-spacing:1px;line-height:1;margin:0;font-weight:400;}
  .script{font-family:"Playball",cursive;color:var(--crimson);line-height:1;margin:0;font-weight:400;text-transform:none;letter-spacing:0;}
  .subtitle{font-family:"Questrial",sans-serif;color:var(--crimson);text-transform:uppercase;letter-spacing:1px;margin:0;}
  .ornament{display:block;margin:0 auto;width:16px;height:14px;border-radius:50% 50% 40% 40%;background:var(--ink);}

  /* back panel */
  .back{position:absolute;left:0;top:0;width:556px;height:879px;}
  .splash{position:absolute;border-radius:50%;}
  .splash--back-top{left:-70px;top:-60px;width:190px;height:200px;background:radial-gradient(circle at 40% 40%,var(--splash-red) 0%,rgba(93,107,42,.7) 45%,rgba(255,255,255,0) 72%);}
  .splash--back-bottom{left:-50px;top:720px;width:200px;height:200px;background:radial-gradient(circle at 45% 55%,var(--splash-dark) 0%,rgba(93,107,42,.75) 35%,rgba(168,50,31,.5) 55%,rgba(255,255,255,0) 72%);}
  .back-title{position:absolute;left:40px;width:480px;top:32px;text-align:center;}
  .back-title .caps{font-size:31px;}
  .back-title .script{font-size:35px;margin:2px 0 4px;}
  .back-title .subtitle{font-size:18px;margin-top:14px;}
  .back-title .ornament{margin-top:14px;}

  .blurb-block{position:absolute;left:62px;width:516px;top:258px;text-align:center;}
  .blurb{font-size:13.6px;line-height:17px;margin:0;}
  .blurb em{font-style:italic;}
  .signature{font-size:12.5px;font-weight:700;font-style:italic;margin:8px 0 0;}

  .author-block{position:absolute;left:62px;top:513px;width:478px;}
  .author-photo{float:left;width:122px;height:122px;margin:0 12px 4px 0;background:linear-gradient(160deg,#c8232a 0%,#b51d24 55%,#6f8c63 100%);}
  .bio{font-size:10.8px;line-height:15.8px;margin:0;text-align:justify;}
  .bio-more{clear:both;font-size:10.8px;line-height:15.8px;margin:0;}
  .isbn-block{position:absolute;left:345px;top:725px;width:196px;height:120px;background:var(--box-red);}

  /* spine */
  .spine{position:absolute;left:556px;top:0;width:88px;height:879px;}
  .spine-text{position:absolute;left:50%;top:26px;height:826px;transform:translateX(-50%);writing-mode:vertical-rl;white-space:nowrap;display:flex;align-items:center;}
  .spine-title{font-size:18px;text-transform:uppercase;letter-spacing:.5px;}
  .spine-title .script{font-size:19px;margin:8px 0;}
  .spine-author{font-size:13px;text-transform:uppercase;letter-spacing:7px;margin-top:26px;}

  /* front panel */
  .front{position:absolute;left:644px;top:0;width:556px;height:879px;}
  .portrait{position:absolute;left:40px;top:0;width:470px;height:450px;border-radius:50%;
    background:radial-gradient(ellipse at 52% 45%,#d9d9d9 0%,var(--portrait-grey) 30%,#4b4b4b 42%,rgba(93,107,42,.85) 52%,rgba(168,50,31,.7) 62%,rgba(255,255,255,0) 72%);}
  .front-title{position:absolute;left:0;width:556px;top:480px;text-align:center;}
  .front-title .caps{font-size:44px;letter-spacing:1.5px;}
  .front-title .script{font-size:48px;margin:0 0 4px;}
  .front-title .subtitle{font-size:20px;margin-top:20px;}
  .front-title .ornament{margin-top:16px;}
  .front-author{position:absolute;left:0;width:556px;top:830px;text-align:center;font-size:18px;letter-spacing:9px;text-transform:uppercase;margin:0;}
</style>
</head>
<body>
<div class="cover">

  <section class="back">
    <div class="splash splash--back-top" role="img" aria-label="Paint splatter in red and olive green"></div>
    <div class="splash splash--back-bottom" role="img" aria-label="Paint splatter in dark brown, olive and red"></div>

    <header class="back-title">
      <h2 class="caps">9 Lanterns</h2>
      <p class="script">Beyond the</p>
      <p class="caps">Quiet Harbor</p>
      <p class="caps" style="margin-top:2px">at Dusk</p>
      <p class="subtitle">Gentle Lessons On Morning Gardens</p>
      <span class="ornament" role="img" aria-label="Small flourish ornament"></span>
    </header>

    <div class="blurb-block">
      <p class="blurb">Abundant Life is experienced as one hears and then puts into practice the Word of God. Jesus emphasized this point that the blessing is in the doing (practice). Jesus said, “<em>But even more blessed are all who hear the word of God and put it into practice</em>” (Luke 11:28 New Living Translation). Also, He said, “<em>Now that you know these things, God will bless you for doing them</em>” (John 13:17 NLT). The point of this book therefore, is to encourage the believer to adopt these Old Testament truths for daily living by making practical everyday decisions to walk in these covenant realities. For <strong>the believer</strong> to realize the Abundant Life (John 10:10), he <strong>must be a practitioner</strong>. Practicing the Word of God is a proven covenant technique for victorious living. I believe you are on your way to living Abundantly and fulfilling your covenant destiny.</p>
      <p class="signature">Dr. Gordon Peltiway, Sr.</p>
    </div>

    <div class="author-block">
      <div class="author-photo" role="img" aria-label="Author portrait photo"></div>
      <p class="bio"><strong>GORDON O. PELTIWAY, SR. Ph.D.</strong>, is Senior Pastor of the Willowmere Bible Fellowship Church, Ashcombe, Vermont. A visionary and a missionary, he has traveled extensively, preaching and lecturing in several countries, and has studied and demonstrated proficiency in various fields such as Theology, Education, Christian Counseling, Writing, Speaking and Applied Sciences, (Biochemistry, Bacteriology &amp; Public Health). Dr. Peltiway is author of online daily devotions, ‘Morning Lantern’, and President of HARBORMEN+, an International Ministry to Men.</p>
      <p class="bio-more">He is president of Willowmere International Ministries and Protestant Minister, for the State of Northvale, Department of Rehabilitation and is an ordained Bishop with the LGFA Ministries, (League of Gospel Fellowship Assemblies, USA). He is blessed with his wife Pastor Mireth and their four children.</p>
    </div>

    <div class="isbn-block"></div>
  </section>

  <section class="spine">
    <div class="spine-text">
      <span class="spine-title">9 Lanterns <span class="script">Beyond the</span> Quiet Harbor at Dusk</span>
      <span class="spine-author">Gordon Peltiway, Sr.</span>
    </div>
  </section>

  <section class="front">
    <div class="portrait" role="img" aria-label="Black and white portrait photo framed by red and green paint splatter"></div>
    <header class="front-title">
      <h1 class="caps">9 Lanterns</h1>
      <p class="script">Beyond the</p>
      <p class="caps">Quiet</p>
      <p class="caps" style="margin-top:4px">Harbor</p>
      <p class="caps" style="margin-top:4px">at Dusk</p>
      <p class="subtitle">Gentle Lessons On Morning Gardens</p>
      <span class="ornament" role="img" aria-label="Small flourish ornament"></span>
    </header>
    <p class="front-author">Gordon Peltiway, Sr.</p>
  </section>

</div>
</body>
</html>
```